Managed Service Provider VOIP Flyer

Looking for a one page US letter size single or double sided brochure to offer cloud hosted VoIP Phone system and unified communications. We have partnered with a VoIP Phone system company and want to sell their services but we don't want their name to be shown on the brochure because customers might call them directly. The company name is Quorvel (www.quorvel-example.com) and our company name is Lumen By Harlow, LLC and our voice product is called Clearly Talk. I have also uploaded my company's logo that you should show on the brochure and use that coloring. For more details about the product, you can visit their website mentioned above. Also I am looking for something very similar to this project and many of the technical details are the same https://flyer.contestpad-example.com/contest/5817264

I have also uploaded a PDF with my different package levels and some of the included features. Depending on the design we may or may not want the package levels on this flyer.

Target Market(s)

Small and medium Businesses

Industry/Entity Type

Voip

Requirements
Must have
• Feature and benefits information of Managed VOICE. Use my logo and coloring from my logo. Include our website, email, phone and possibly facebook if it makes sense/looks good.

www.lumenbyharlow-example.com
415.836.0.917
sales@lumenbyharlow-example.com
www.socialsite-example.com/lumenbyharlow
Nice to have
• Would like to show how the service is simple and reliable and available for any business size

```html
<!DOCTYPE html>
<html lang="en">
<head>
<meta charset="utf-8">
<title>Lumen By Harlow – Clearly Talk Flyer</title>
<link rel="stylesheet" href="https://fonts.googleapis.com/css2?family=Bebas+Neue&family=Oswald:wght@500;600&family=Inter:wght@400;500;600;700&display=swap">
<style>
  :root{
    --navy:#14295a;
    --navy-deep:#0e1d44;
    --navy-mid:#1d3a78;
    --red:#c0312b;
    --red-soft:#c64841;
    --red-dark:#b32a24;
    --ink:#1b1f2e;
    --muted:#8a8f99;
    --stripe:#eeeff1;
    --bg:#dcdcde;
    --paper:#ffffff;
  }
  *{box-sizing:border-box;margin:0;padding:0}
  html,body{width:1200px;height:743px;overflow:hidden;background:var(--bg);font-family:"Inter",sans-serif;color:var(--ink)}
  .page{position:absolute;top:94px;width:433px;height:558px;background:var(--paper);overflow:hidden;box-shadow:0 6px 14px rgba(0,0,0,.12)}
  .page--front{left:139px}
  .page--back{left:630px}

  /* front header */
  .brand{position:absolute;left:32px;top:14px;display:flex;align-items:center;gap:6px}
  .brand__mark{width:18px;height:18px;background:var(--red)}
  .brand__name{font-weight:600;font-size:9px;color:var(--navy);letter-spacing:.3px}
  .top-contact{position:absolute;right:33px;top:17px;text-align:right;font-size:6.6px;line-height:10px;color:var(--navy)}
  .top-contact b{color:var(--red);font-weight:700;margin-right:3px}

  .hero-photo{position:absolute;left:166px;top:59px;width:267px;height:192px;background:linear-gradient(120deg,#cfe3f0 0%,#e8f2f8 45%,#b9d3e6 100%)}
  .hero-shape{position:absolute;left:0;top:50px}
  .hero-kicker{position:absolute;left:0;top:91px;height:23px;width:217px;background:var(--red);clip-path:polygon(0 0,100% 0,93% 100%,0 100%);color:#fff;font-size:12px;line-height:23px;padding-left:32px;letter-spacing:.2px}
  .hero-title{position:absolute;left:32px;top:122px;font-family:"Bebas Neue",sans-serif;font-weight:400;font-size:34px;line-height:33px;color:#fff;letter-spacing:.5px}

  .section-title{font-weight:700;font-size:10px;color:var(--red);letter-spacing:.2px}
  .products{position:absolute;left:32px;top:283px;width:162px}
  .products p{margin-top:9px;font-size:8px;line-height:11.3px}
  .products p em{font-style:normal;color:var(--navy-mid);font-weight:500}
  .service{position:absolute;left:32px;display:flex;gap:10px;width:160px}
  .service__icon{flex:none;width:22px;height:22px}
  .service h4{font-size:7px;font-weight:700;color:var(--navy);margin-bottom:3px}
  .service p{font-size:6.6px;line-height:9.5px}

  .what{position:absolute;left:227px;top:272px;width:180px}
  .what p{margin-top:9px;font-size:8px;line-height:11.3px}
  .benefits{position:absolute;left:227px;top:334px;width:185px;height:224px}
  .benefit{position:absolute;left:0;width:185px;color:#fff;padding:14px 14px 0 34px}
  .benefit h4{font-size:8.4px;font-weight:600;margin-bottom:6px}
  .benefit p{font-size:6.6px;line-height:9.3px}
  .benefit--one{top:0;height:77px;background:var(--red-soft)}
  .benefit--two{top:77px;height:69px;background:#bd3a33}
  .benefit--three{top:146px;height:78px;background:var(--red-dark)}
  .badge{position:absolute;left:-20px;width:40px;height:40px;border-radius:50%;background:var(--navy);display:flex;align-items:center;justify-content:center}

  /* back */
  .packages-title{position:absolute;left:32px;top:40px;font-family:"Oswald",sans-serif;font-weight:600;font-size:16.5px;color:var(--red);letter-spacing:.3px}
  .plan{position:absolute;top:32px;width:82px;height:35px;border-radius:2px;color:#fff;text-align:center;padding-top:7px}
  .plan strong{display:block;font-size:8.4px;font-weight:600}
  .plan span{display:block;font-size:6.6px;margin-top:3px}
  .plan--primer{left:148px;background:#1f3f80}
  .plan--standard{left:232px;background:#1a3470}
  .plan--premium{left:317px;background:var(--navy-deep)}
  .features{position:absolute;left:32px;top:71px;width:367px;border-collapse:collapse;font-size:6.9px}
  .features td{height:16px;padding:0 0 0 8px}
  .features td:not(:first-child){text-align:center;padding:0;width:84px}
  .features tr:nth-child(odd){background:var(--stripe)}
  .features tr.price td{height:24px;font-size:8.4px;font-weight:700;color:var(--navy)}
  .features tr.tall td{height:27px;line-height:11px}
  .features .no{color:var(--muted)}
  .footer-band{position:absolute;left:0;bottom:0}
  .footer-text{position:absolute;left:30px;right:30px;top:523px;text-align:center;color:#fff;font-size:7.4px;line-height:12.5px;white-space:nowrap}
  .footer-text b{font-weight:700;margin-left:6px}
</style>
</head>
<body>

<section class="page page--front">
  <div class="brand"><span class="brand__mark"></span><span class="brand__name">LUMEN BY HARLOW</span></div>
  <div class="top-contact">
    <div><b>W</b>www.lumenbyharlow-example.com</div>
    <div><b>P</b>415.836.0.917 | <b style="margin-left:2px">E</b>sales@lumenbyharlow-example.com</div>
  </div>

  <div class="hero-photo" role="img" aria-label="Photo of a smiling customer support agent wearing a headset at a computer in a bright office"></div>
  <svg class="hero-shape" width="270" height="213" viewBox="0 0 270 213">
    <defs><linearGradient id="heroFill" x1="0" y1="0" x2="1" y2="1"><stop offset="0" stop-color="#0e1d44"/><stop offset="1" stop-color="#1d3a78"/></linearGradient></defs>
    <path d="M0 0 H258 Q266 0 262 8 L164 200 Q157 212 144 212 H0 Z" fill="url(#heroFill)"/>
  </svg>
  <div class="hero-kicker">THE NEXT GENERATION OF</div>
  <h1 class="hero-title">COMMUNICATION<br>FOR YOUR<br>BUSINESS</h1>

  <div class="products">
    <h2 class="section-title">OUR PRODUCTS &amp; APIS</h2>
    <p>We offer a portfolio of business communication services and APIs delivered via our Clearly Talk tier 1 carrier network including <em>SIP Trunking, UCaaS, Messaging, Fax and Data services.</em></p>
  </div>

  <div class="service" style="top:381px">
    <svg class="service__icon" viewBox="0 0 22 22"><path d="M11 1 L20 6 V16 L11 21 L2 16 V6Z" fill="#f6dede"/><path d="M6 15 A6 6 0 1 1 16 13" fill="none" stroke="#14295a" stroke-width="1.4"/><path d="M14 11 L16 13.5 L18 11" fill="none" stroke="#14295a" stroke-width="1.4"/></svg>
    <div><h4>SIP TRUNKING</h4><p>High quality, affordable Tier 1 voice services that are easy and fast to deploy</p></div>
  </div>
  <div class="service" style="top:438px">
    <svg class="service__icon" viewBox="0 0 22 22"><path d="M11 1 L20 6 V16 L11 21 L2 16 V6Z" fill="#f6dede"/><path d="M11 20 V11 L6 6 M11 11 L16 6 M6 6 V9 M6 6 H9 M16 6 V9 M16 6 H13" fill="none" stroke="#14295a" stroke-width="1.3"/></svg>
    <div><h4>UNIFIED COMMUNICATIONS</h4><p>Cloud-based business communications giving you on-the-go availability on any device</p></div>
  </div>
  <div class="service" style="top:494px">
    <svg class="service__icon" viewBox="0 0 22 22"><path d="M11 1 L20 6 V16 L11 21 L2 16 V6Z" fill="#f6dede"/><rect x="5" y="9" width="12" height="7" fill="none" stroke="#14295a" stroke-width="1.3"/><rect x="7.5" y="5" width="7" height="4" fill="none" stroke="#14295a" stroke-width="1.3"/><rect x="7.5" y="14" width="7" height="5" fill="#fff" stroke="#14295a" stroke-width="1.3"/></svg>
    <div><h4>FAX</h4><p>Secure, dependable and cost-effective document faxing from anywhere</p></div>
  </div>

  <div class="what">
    <h2 class="section-title">WHAT WE DO</h2>
    <p>We delivers simple and smart communication services enabling businesses to communicate whenever, whereever and however they want.</p>
  </div>

  <div class="benefits">
    <div class="benefit benefit--one">
      <h4>High Quality Mode</h4>
      <p>Largest on-net phone number footprint in the US with 90%+ of calls originating and terminating on-net, achieving industry leading 97% call completion.</p>
    </div>
    <div class="benefit benefit--two">
      <h4>Ease of Use</h4>
      <p>100% self-service via our Admin Portal and APIs, backed by the support of our Service Delivery teams.</p>
    </div>
    <div class="benefit benefit--three">
      <h4>Cost-Effective</h4>
      <p>As a Tier 1 Carrier, we help you eliminate the middleman and saving your business 20-40% on your existing communication service.</p>
    </div>
    <div class="badge" style="top:19px"><svg width="22" height="22" viewBox="0 0 22 22"><circle cx="11" cy="11" r="9" fill="none" stroke="#fff" stroke-width="1.2" stroke-dasharray="3 1.5"/><circle cx="11" cy="11" r="6" fill="none" stroke="#fff" stroke-width="1.2"/><path d="M8 11 L10 13 L14 9" fill="none" stroke="#fff" stroke-width="1.3"/></svg></div>
    <div class="badge" style="top:92px"><svg width="22" height="22" viewBox="0 0 22 22"><circle cx="11" cy="8" r="5" fill="none" stroke="#fff" stroke-width="1.2"/><path d="M4 20 Q11 12 18 20" fill="none" stroke="#fff" stroke-width="1.2"/><path d="M5 9 V7 Q11 0 17 7 V9" fill="none" stroke="#fff" stroke-width="1.2"/></svg></div>
    <div class="badge" style="top:168px"><svg width="22" height="22" viewBox="0 0 22 22"><circle cx="12" cy="8" r="5" fill="none" stroke="#fff" stroke-width="1.2"/><text x="12" y="10.5" font-size="7" fill="#fff" text-anchor="middle" font-family="Inter,sans-serif">$</text><path d="M2 16 H7 L12 18 L19 14" fill="none" stroke="#fff" stroke-width="1.2"/></svg></div>
  </div>
</section>

<section class="page page--back">
  <h2 class="packages-title">OUR PACKAGES</h2>
  <div class="plan plan--primer"><strong>Primer</strong><span>(Location, not a user)</span></div>
  <div class="plan plan--standard"><strong>Standard</strong><span>(Basic user)</span></div>
  <div class="plan plan--premium"><strong>Premium</strong><span>(Power user)</span></div>

  <table class="features">
    <tr class="price"><td>Monthly Price</td><td>$20</td><td>$30</td><td>$35</td></tr>
    <tr><td>Extension Dialing</td><td>Yes</td><td>Yes</td><td>Yes</td></tr>
    <tr><td>Local Outbound Calls Only</td><td>Yes</td><td>LD Included</td><td>LD Included</td></tr>
    <tr class="tall"><td>Caller ID and Caller Name<br>Delivery</td><td>Yes</td><td>Yes</td><td>Yes</td></tr>
    <tr><td>Call Logs</td><td>Yes</td><td>Yes</td><td>Yes</td></tr>
    <tr><td>Last Number Redial</td><td>Yes (Local Only)</td><td>Yes</td><td>Yes</td></tr>
    <tr><td>Music On Hold</td><td>Yes</td><td>Yes</td><td>Yes</td></tr>
    <tr><td>Corporate Directory Access</td><td>Yes</td><td>Yes</td><td>Yes</td></tr>
    <tr><td>E911 Service</td><td>Yes</td><td>Yes</td><td>Yes</td></tr>
    <tr><td>Call Park</td><td class="no">No</td><td>Yes</td><td>Yes</td></tr>
    <tr class="tall"><td>Call Forwarding (Always, Busy,<br>No-Answer, Not Reachable)</td><td class="no">No</td><td>Yes</td><td>Yes</td></tr>
    <tr><td>Call Recording</td><td class="no">No</td><td>Additional</td><td>Additional</td></tr>
    <tr><td>Call Transfer</td><td class="no">No</td><td>Yes</td><td>Yes</td></tr>
    <tr><td>Call Waiting</td><td class="no">No</td><td>Yes</td><td>Yes</td></tr>
    <tr><td>Unified Messaging</td><td class="no">No</td><td>Yes</td><td>Yes</td></tr>
    <tr><td>Inclusion in Hunt Groups</td><td class="no">No</td><td>Yes</td><td>Yes</td></tr>
    <tr><td>Simultaneous Ring</td><td class="no">No</td><td>Yes</td><td>Yes</td></tr>
    <tr><td>Sequential Ring</td><td class="no">No</td><td>Yes</td><td>Yes</td></tr>
    <tr><td>Speed Dial 100</td><td class="no">No</td><td>Yes</td><td>Yes</td></tr>
    <tr><td>Three-Way Calling</td><td class="no">No</td><td>Yes</td><td>Yes</td></tr>
    <tr><td>Nexdesk Client</td><td class="no">No</td><td class="no">No</td><td>Yes</td></tr>
    <tr><td>Desktop Sharing</td><td class="no">No</td><td class="no">No</td><td>Yes</td></tr>
    <tr><td>Web Collaboration</td><td class="no">No</td><td class="no">No</td><td>Yes</td></tr>
  </table>

  <svg class="footer-band" width="433" height="52" viewBox="0 0 433 52">
    <defs><linearGradient id="footFill" x1="0" y1="0" x2="1" y2="0"><stop offset="0" stop-color="#0e1d44"/><stop offset="1" stop-color="#1d3a78"/></linearGradient></defs>
    <path d="M40 0 H393 Q398 0 396 3 L38 3 Q36 0 40 0Z" fill="#c0312b"/>
    <path d="M30 4 H403 Q408 4 411 9 L426 52 H6 L24 9 Q26 4 30 4Z" fill="url(#footFill)"/>
  </svg>
  <div class="footer-text">
    <div><b style="margin-left:0">W</b> www.lumenbyharlow-example.com <b>P</b> 415.836.0.917 <b>E</b> sales@lumenbyharlow-example.com</div>
    <div>www.socialsite-example.com/lumenbyharlow</div>
  </div>
</section>

</body>
</html>
```